India March 15 Flyer

I would like a A4 Flyer made.
Very similair to attached file but the following changes
Name would be Wander India Fabric & Flavour Journey

Cost $6995.00pp
16days fully escorted
Breakfast & Dinner included for 15days
Tour Departs Auckland 15th March 2015

Take out anything that is associated to Corbel Globe Voyages and it should be KiwiTrip Agents (attached) file for this.
Also no address just phone no's which is
09 358 6172
021637294
maren@kiwitripagents.example.nz
KiwiTrip Agents Support Office:
Level 4, Quorn Plaza House, 3-21 Bellamy Rd,
Palmerston North 4410
Web:www.kiwitripagents.example.nz
Under conditions take out Corbel Globe Voyages and put in KiwiTrip Agents and prices correct as at 20August 2014.
Under Conditions please change $400 deposit to $500 deposit pp.
Under Conditions: Price is Share Twin. Please advise if you want a single supplement cost.
I have attached a flyer that was done for me when i did the last tour. So this will give you an idea.
Also have attached the current itinerary that we will be doing for the March 2015 tour.
Hope this is enough information
Updates

Hello, Please do not forget to do the back of the flyer. dont put in itinerary but maybe a picture of the region that we are traveling and the Terms and Conditions which is so important. Thanks

I have noticed that the designs comming through dont have fully escorted by Maren Thistle which is a part of the brief with the flyer I included. Also return flights etc. Everything that was on the orginal flyer needs to include all of this except the Corbel Globe Voyages.

as this is a textile and culinary tour i would like to see pictures of textiles and food, as well as the normal pictures of India. I only seem to be getting elephant, taj extra but need to show the tour i am selling. Many thanks

Please re read the brief as i have made the required changes on this. IE: Price is now changed as well as some Terms and Conditions

Requirements
Must have
• About Maren Thistle
Nice to have
• Pictures of Textiles and Culinerary as well as monuments

```html
<!DOCTYPE html>
<html lang="en">
<head>
<meta charset="utf-8">
<title>Wander India – Fabric &amp; Flavour Journey Flyer</title>
<link rel="stylesheet" href="https://fonts.googleapis.com/css2?family=Great+Vibes&family=Open+Sans:wght@400;600;700;800&display=swap">
<style>
:root{
  --bg:#e9e7e2;
  --leaf:#8cc63f;
  --leaf-dark:#6aa22a;
  --mint:#d6e8b4;
  --mint-pale:#e7f1d2;
  --mint-row:#cfe3a6;
  --price-green:#c9e2a0;
  --ink:#1d1d1b;
  --ink-soft:#3b3b38;
  --white:#ffffff;
}
*{box-sizing:border-box;margin:0;padding:0}
html,body{width:1200px;height:900px;overflow:hidden;background:var(--bg);font-family:"Open Sans",Arial,sans-serif;color:var(--ink)}
.canvas{position:relative;width:1200px;height:900px}

.flyer{position:absolute;width:470px;height:665px;overflow:hidden;box-shadow:0 6px 18px rgba(0,0,0,.18)}
.flyer--back{left:85px;top:118px;background:linear-gradient(180deg,var(--mint-pale),var(--mint))}
.flyer--front{left:645px;top:118px;background:var(--white)}

/* back page */
.back-header{position:absolute;left:120px;top:26px;width:330px;height:82px;border-radius:41px 0 0 41px;background:rgba(255,255,255,.6)}
.back-title{position:absolute;left:205px;top:34px;width:240px;font-family:"Great Vibes",cursive;font-weight:400;font-size:30px;line-height:30px;color:var(--ink-soft);text-align:center}
.region-map{position:absolute;left:12px;top:24px;width:166px;height:166px;border-radius:50%;background:var(--leaf);border:5px solid var(--white)}
.photo-circle{position:absolute;border-radius:50%;border:5px solid var(--white);width:136px;height:136px}
.photo-spice{left:44px;top:192px;background:radial-gradient(circle at 40% 60%,#b5401d,#d98a3a 55%,#8a3a1c)}
.photo-weaver{left:26px;top:318px;background:linear-gradient(135deg,#6a5a7a,#c7b08a 50%,#4f7a8c)}
.photo-food{left:44px;top:444px;background:radial-gradient(circle at 50% 40%,#e2b85a,#a8762e 60%,#5e6b2a)}

.itinerary{position:absolute;left:190px;top:118px;width:272px}
.itinerary h2{font-size:10px;font-weight:800;letter-spacing:.2px;margin:0 0 4px 6px}
.day{font-size:7.6px;line-height:10.5px;padding:2px 6px 3px;color:var(--ink-soft)}
.day:nth-child(odd){background:var(--mint-row)}
.day b{color:var(--ink);font-weight:700}

.back-footer{position:absolute;left:0;bottom:0;width:100%;height:100px;background:var(--white)}
.contact{position:absolute;left:60px;top:9px;font-size:8px;font-weight:700;line-height:12px;white-space:nowrap}
.conditions{position:absolute;left:14px;top:40px;width:215px;font-size:5.2px;line-height:7px;color:var(--ink-soft)}

.brand{position:absolute;display:flex;flex-direction:column;align-items:flex-end;z-index:3}
.brand-row{display:flex;align-items:center;gap:6px}
.brand-dot{width:14px;height:14px;border-radius:50%;background:var(--leaf)}
.brand-name{font-weight:800;color:var(--ink);letter-spacing:-.5px;white-space:nowrap}
.brand-agent{font-weight:800;color:var(--leaf-dark)}
.back-footer .brand{right:16px;top:40px}
.back-footer .brand-name{font-size:20px}
.back-footer .brand-agent{font-size:10px}

/* front page */
.hero{position:absolute;left:0;top:0;width:470px;height:560px;background:
  linear-gradient(100deg,rgba(30,60,150,.6),rgba(0,0,0,0) 40%),
  linear-gradient(180deg,#c6244a 0%,#e0582a 25%,#7a2f8a 55%,#2f5aa0 80%,#3e3640 100%)}
.hero-curves{position:absolute;left:0;top:0}
.front-title{position:absolute;right:24px;top:40px;text-align:right;color:var(--white)}
.front-title h1{font-family:"Great Vibes",cursive;font-weight:400;font-size:50px;line-height:50px}
.front-title p{font-size:10.5px;letter-spacing:1px;font-weight:600;margin-top:2px;text-transform:uppercase}
.price-circle{position:absolute;left:-14px;top:410px;width:270px;height:270px;border-radius:50%;background:var(--price-green);padding:46px 18px 0 34px;z-index:1}
.intro-circle{position:absolute;left:20px;top:262px;width:170px;height:170px;border-radius:50%;background:var(--leaf);color:var(--white);padding:30px 20px 0 22px;z-index:2}
.intro-circle h3{font-family:"Great Vibes",cursive;font-weight:400;font-size:21px;line-height:24px;margin-bottom:3px}
.intro-circle p{font-size:7.8px;line-height:10px;font-weight:600}
.price{display:flex;align-items:flex-end;gap:8px}
.price strong{font-size:31px;font-weight:800;line-height:31px}
.price strong sup{font-size:15px}
.price small{font-size:7px;font-weight:700}
.price span{font-size:8px;font-weight:700;line-height:10px;text-transform:uppercase}
.inclusions{display:flex;gap:12px;margin-top:8px;width:215px}
.inclusions ul{list-style:none;flex:1;font-size:7.6px;line-height:9.6px;font-weight:600}
.inclusions li{margin-bottom:4px}
.inclusions li::before{content:"\2022  ";font-weight:800}
.departs{margin-top:6px;text-align:center;width:215px;font-size:8px;font-weight:700;line-height:10.5px;text-transform:uppercase}
.flyer--front .brand{right:20px;bottom:22px}
.flyer--front .brand-name{font-size:24px}
.flyer--front .brand-agent{font-size:11px}
</style>
</head>
<body>
<main class="canvas">

  <section class="flyer flyer--back" aria-label="Flyer back: itinerary">
    <div class="back-header"></div>
    <h2 class="back-title">A Fabric &amp; Flavour Journey</h2>
    <div class="region-map" role="img" aria-label="Map of northern India marking the tour stops"></div>
    <div class="photo-circle photo-spice" role="img" aria-label="Photo of heaped red and orange spice powders"></div>
    <div class="photo-circle photo-weaver" role="img" aria-label="Photo of a woman weaving textiles on a loom"></div>
    <div class="photo-circle photo-food" role="img" aria-label="Photo of bowls of Indian street food"></div>

    <div class="itinerary">
      <h2>ITINERARY OVERVIEW</h2>
      <div class="day"><b>15 March - Arrive Delhi</b> m fuga. Nequi cone quis sit fugition et lande statum ducidunti quas quo bearcip saepern aturio esequiam</div>
      <div class="day"><b>16 March - In Delhi</b> m fuga. Nequi cone quis sit fugition et lande statum ducidunti quas quo bearcip saepern aturio esequiam</div>
      <div class="day"><b>17 March - Delhi - Lucknow</b> m fuga. Nequi cone quis sit fugition et lande statum ducidunti quas quo bearcip saepern</div>
      <div class="day"><b>18 March - Lucknow</b> m fuga. Nequi cone quis sit fugition et lande statum ducidunti quas quo bearcip saepern aturio esequiam</div>
      <div class="day"><b>19 March - Lucknow - Varanasi</b> m fuga. Nequi cone quis sit fugition et lande statum ducidunti quas quo bearcip saepern aturio esequiam</div>
      <div class="day"><b>20 March - Varanasi - Agra</b> m fuga. Nequi cone quis sit fugition et lande statum ducidunti quas quo bearcip saepern aturio</div>
      <div class="day"><b>21 March - Arrive Agra</b> m fuga. Nequi cone quis sit fugition et lande statum ducidunti quas quo bearcip saepern aturio esequiam</div>
      <div class="day"><b>22 March - Agra</b> m fuga. Nequi cone quis sit fugition et lande statum ducidunti quas quo bearcip saepern aturio esequiam</div>
      <div class="day"><b>23 March - Agra - Jaipur</b> m fuga. Nequi cone quis sit fugition et lande statum ducidunti quas quo bearcip saepern aturio esequiam</div>
      <div class="day"><b>24 March - Jaipur</b> m fuga. Nequi cone quis sit fugition et lande statum ducidunti quas quo bearcip saepern aturio</div>
      <div class="day"><b>25 March - Jaipur</b> m fuga. Nequi cone quis sit et lande statum ducidunti quas quo bearcip saepern aturio esequiam</div>
      <div class="day"><b>26 March - Jaipur - Jodhpur</b> m fuga. Nequi cone quis sit fugition et lande statum ducidunti quas quo aturio esequiam</div>
      <div class="day"><b>27 March - Jodhpur</b> m fuga. Nequi cone quis sit fugition et lande statum ducidunti quas quo bearcip saepern atur</div>
      <div class="day"><b>28 March - Jodhpur - Ranakpur - Udaipur</b> m fuga. Nequi cone quis sit fugition et lande statum ducidunti quas quo bearcip saepern</div>
      <div class="day"><b>29 March - Udaipur</b> m fuga. Nequi cone quis sit fugition et lande statum ducidunti quas quo bearcip saepern aturio esequiam</div>
      <div class="day"><b>30 March - Udaipur - Mumbai - Auckland</b> m fuga. Nequi cone quis</div>
    </div>

    <footer class="back-footer">
      <p class="contact">Contact Maren: maren@kiwitripagents.example.nz Ph: 09 358 6172 Mob: 021637294<br>www.kiwitripagents.example.nz</p>
      <p class="conditions">Conditions apply: price per person share twin from Auckland in economy class, valid for the departure shown. Minimum of ten guests required for the tour to proceed. A deposit of $500 per person secures your seat. Prices correct as at 20 August 2014 and may change due to currency or fuel surcharges. Single supplement available on request. Please ask us for full terms.</p>
      <div class="brand">
        <div class="brand-row"><span class="brand-dot"></span><span class="brand-name">KiwiTrip Agents</span></div>
        <span class="brand-agent">Maren Thistle</span>
      </div>
    </footer>
  </section>

  <section class="flyer flyer--front" aria-label="Flyer front: Wander India">
    <div class="hero" role="img" aria-label="Photo of a woman at a market stall hung with colourful embroidered textiles"></div>
    <svg class="hero-curves" width="470" height="665" viewBox="0 0 470 665" aria-hidden="true">
      <path d="M0 0H160C90 10 30 40 0 80Z" fill="var(--white)"/>
      <path d="M0 0H120C70 8 25 30 0 60Z" fill="var(--leaf)"/>
      <path d="M470 470V560H330C390 540 440 510 470 470Z" fill="var(--leaf)"/>
      <path d="M470 500V560H380C420 550 450 530 470 500Z" fill="var(--white)"/>
      <rect x="0" y="560" width="470" height="105" fill="var(--white)"/>
    </svg>
    <div class="front-title">
      <h1>Wander India</h1>
      <p>Fabric &amp; Flavour Journey</p>
    </div>
    <div class="price-circle">
      <div class="price">
        <strong>$6995<sup>*</sup></strong><small>pp</small>
        <span>16 days fully escorted<br>with Maren Thistle</span>
      </div>
      <div class="inclusions">
        <ul>
          <li>Return Airfares Auckland to Delhi/ Mumbai to Auckland Direct</li>
          <li>15 nights Accommodation</li>
        </ul>
        <ul>
          <li>Local travel and transfers</li>
          <li>Breakfast &amp; Dinner for 15 days</li>
          <li>Sightseeing and entrance to selected monuments</li>
        </ul>
      </div>
      <p class="departs">Tour departs Auckland<br>15th March 2015</p>
    </div>
    <div class="intro-circle">
      <h3>India Tours</h3>
      <p>We'll take you to the rich cities in history and monumental splendour. Taking in all the wealth of Indian culture and of course the rich variety of textile crafts.</p>
    </div>
    <div class="brand">
      <div class="brand-row"><span class="brand-dot"></span><span class="brand-name">KiwiTrip Agents</span></div>
      <span class="brand-agent">Maren Thistle</span>
    </div>
  </section>

</main>
</body>
</html>
```